Bottled Beer Label Design

See Attached.
Updates
The beer label is printed on transparent pvc sticker, like the Valdermoor label. It meant that the unprinted part will be the color of the bottle. In this case it is amber color.
Attached please find photos of Valdermoor Bottle and label.
Thank you and best of luck.
Target Market(s)
Cater to the age grpoup in the 20's to early 40's in the Pubs and tothe la
Requirements
Must have
- See Attached.
Nice to have
- See Attached.
Should not have
- prefer not to have odd shaped label as the manufacturing will be easy and thus cheaper, and application of the label on to the bottle is less liable to develop defects

```html
<!DOCTYPE html>
<html lang="en">
<head>
<meta charset="utf-8">
<title>Halvern Brew House – Beer Label</title>
<link rel="stylesheet" href="https://fonts.googleapis.com/css2?family=Cinzel:wght@700;900&family=Yellowtail&display=swap">
<style>
  :root {
    --label-red: #d3141c;
    --gold: #e3c98a;
    --gold-light: #f3e2b0;
    --gold-dark: #b8975a;
    --parchment: #e8d9a8;
    --parchment-dark: #c9b27a;
    --banner-white: #ffffff;
    --ribbon-shade: #ececec;
    --brand-red: #d8262d;
    --page: #ffffff;
  }
  html, body {
    margin: 0;
    padding: 0;
    width: 1200px;
    height: 862px;
    overflow: hidden;
    background: var(--page);
  }
  .canvas {
    position: relative;
    width: 1200px;
    height: 862px;
  }
  .beer-label {
    position: absolute;
    left: 0;
    top: 0;
  }
  .brand-name {
    font-family: "Cinzel", serif;
    font-weight: 900;
    font-size: 90px;
    fill: var(--brand-red);
  }
  .tagline {
    font-family: "Yellowtail", cursive;
    font-size: 27px;
    fill: var(--banner-white);
  }
  .ribbon-text {
    font-family: "Cinzel", serif;
    font-weight: 700;
    font-size: 34px;
    fill: var(--brand-red);
    letter-spacing: 1px;
  }
</style>
</head>
<body>
<main class="canvas">
  <svg class="beer-label" width="1200" height="862" viewBox="0 0 1200 862" aria-label="Halvern Brew House beer label">
    <defs>
      <linearGradient id="goldPanel" x1="0" y1="0" x2="0" y2="1">
        <stop offset="0" stop-color="#d9bc72"/>
        <stop offset="0.5" stop-color="#efd9a0"/>
        <stop offset="1" stop-color="#c9a75e"/>
      </linearGradient>
      <linearGradient id="mapTone" x1="0" y1="0" x2="1" y2="1">
        <stop offset="0" stop-color="#e8d9a8"/>
        <stop offset="1" stop-color="#c9b27a"/>
      </linearGradient>
      <linearGradient id="wheatTone" x1="0" y1="0" x2="0" y2="1">
        <stop offset="0" stop-color="#d9402f"/>
        <stop offset="1" stop-color="#b5231c"/>
      </linearGradient>
      <clipPath id="archClip">
        <path d="M118 345 L118 300 C118 110 582 110 582 300 L582 345 Z"/>
      </clipPath>
    </defs>

    <rect class="label-body" x="18" y="0" width="664" height="862" rx="22" fill="var(--label-red)"/>
    <rect class="label-frame" x="29" y="36" width="640" height="796" rx="20" fill="none" stroke="var(--gold)" stroke-width="9"/>

    <g class="stars" fill="var(--banner-white)">
      <polygon transform="translate(200 124)" points="0,-16 4.7,-5 16,-5 7,2 10.5,14 0,7 -10.5,14 -7,2 -16,-5 -4.7,-5"/>
      <polygon transform="translate(271 103)" points="0,-16 4.7,-5 16,-5 7,2 10.5,14 0,7 -10.5,14 -7,2 -16,-5 -4.7,-5"/>
      <polygon transform="translate(345 94)" points="0,-16 4.7,-5 16,-5 7,2 10.5,14 0,7 -10.5,14 -7,2 -16,-5 -4.7,-5"/>
      <polygon transform="translate(419 103)" points="0,-16 4.7,-5 16,-5 7,2 10.5,14 0,7 -10.5,14 -7,2 -16,-5 -4.7,-5"/>
      <polygon transform="translate(485 124)" points="0,-16 4.7,-5 16,-5 7,2 10.5,14 0,7 -10.5,14 -7,2 -16,-5 -4.7,-5"/>
    </g>

    <path class="arch-frame" d="M108 345 L108 300 C108 100 592 100 592 300 L592 345" fill="none" stroke="var(--gold)" stroke-width="6"/>
    <rect class="map-area" x="118" y="130" width="464" height="215" clip-path="url(#archClip)" fill="url(#mapTone)" role="img" aria-label="Antique map of Southeast Asia with Singapore marked"/>

    <path class="lower-panel" d="M108 495 L592 495 L592 700 C592 780 108 780 108 700 Z" fill="url(#goldPanel)" stroke="var(--gold-light)" stroke-width="6"/>
    <path class="wheat wheat-left" d="M150 520 C110 570 112 640 170 700 L205 690 C160 640 160 580 190 530 Z" fill="url(#wheatTone)" role="img" aria-label="Wheat sprig ornament"/>
    <path class="wheat wheat-right" d="M550 520 C590 570 588 640 530 700 L495 690 C540 640 540 580 510 530 Z" fill="url(#wheatTone)" role="img" aria-label="Wheat sprig ornament"/>

    <rect class="banner-tab" x="18" y="398" width="664" height="62" rx="8" fill="var(--banner-white)" stroke="var(--gold)" stroke-width="4"/>
    <rect class="banner-frame" x="34" y="342" width="632" height="162" fill="var(--gold-light)"/>
    <rect class="banner" x="40" y="348" width="620" height="150" fill="var(--banner-white)" stroke="var(--gold)" stroke-width="2"/>
    <circle cx="45" cy="429" r="5" fill="var(--label-red)"/>
    <circle cx="637" cy="429" r="5" fill="var(--label-red)"/>
    <text class="brand-name" x="350" y="458" text-anchor="middle" textLength="500" lengthAdjust="spacingAndGlyphs">HALVERN</text>

    <g class="tagline-block">
      <text class="tagline" x="340" y="552" text-anchor="middle">Premium beer, handcrafted</text>
      <text class="tagline" x="340" y="584" text-anchor="middle">from the finest ingredients.</text>
      <text class="tagline" x="340" y="615" text-anchor="middle">Proudly brewed and bottled</text>
      <text class="tagline" x="340" y="645" text-anchor="middle">in Singapore.</text>
    </g>

    <g class="ribbon" transform="rotate(-8 340 725)">
      <path d="M112 705 L178 705 L178 775 L112 775 L132 740 Z" fill="var(--ribbon-shade)" stroke="var(--gold-dark)" stroke-width="1.5"/>
      <path d="M568 705 L502 705 L502 775 L568 775 L548 740 Z" fill="var(--ribbon-shade)" stroke="var(--gold-dark)" stroke-width="1.5"/>
      <rect x="150" y="690" width="380" height="70" fill="var(--banner-white)" stroke="var(--gold-dark)" stroke-width="1.5"/>
      <text class="ribbon-text" x="340" y="738" text-anchor="middle">BREW HOUSE</text>
    </g>
  </svg>
</main>
</body>
</html>
```